Packaging Design for a Quenby sweets company.

We need a packaging design for a new company based in Kuwait named Quenby. We sell trifles in mini sizes and large sizes. (google what a trifle looks like)

I've already attached what the box looks like along with the layouts. All that is needed is drawing on the box.

It Company

• Must have Instagram and Whatsapp/phone number on the box.

Instagram account: quenby_z4
whatsapp/phone: 95318460

```html
<!DOCTYPE html>
<html lang="en">
<head>
<meta charset="utf-8">
<title>Quenby – box dieline</title>
<link rel="stylesheet" href="https://fonts.googleapis.com/css2?family=Fira+Sans:wght@400;500&display=swap">
<style>
  :root {
    --box-blue: #adc6e7;
    --paper-white: #ffffff;
    --fold-line: #1a1a1a;
    --wordmark-grey: #8d8c8f;
    --logo-pink: #f2b2bf;
  }
  html, body {
    margin: 0;
    padding: 0;
    overflow: hidden;
    background: var(--box-blue);
  }
  .dieline {
    position: relative;
    width: 1200px;
    height: 962px;
    background: var(--box-blue);
    overflow: hidden;
    font-family: "Fira Sans", Arial, sans-serif;
  }
  .artwork {
    position: absolute;
    inset: 0;
  }
  .brand {
    position: absolute;
    left: 380px;
    top: 297px;
    width: 440px;
    text-align: center;
  }
  .brand-mark {
    display: block;
    width: 190px;
    height: 190px;
    margin: 0 auto;
    background: var(--logo-pink);
  }
  .brand-name {
    display: block;
    margin-top: 36px;
    color: var(--wordmark-grey);
    font-size: 104px;
    font-weight: 400;
    letter-spacing: 0.28em;
    line-height: 1;
    padding-left: 0.28em;
  }
  .contact {
    position: absolute;
    width: 150px;
    height: 72px;
    margin-left: -75px;
    margin-top: -36px;
    display: flex;
    flex-direction: column;
    justify-content: space-between;
    color: var(--paper-white);
    font-size: 20px;
    font-weight: 500;
    line-height: 28px;
  }
  .contact-row {
    display: flex;
    align-items: center;
    gap: 8px;
  }
  .icon-handle {
    width: 22px;
    height: 22px;
    box-sizing: border-box;
    border: 3px solid var(--paper-white);
    border-radius: 5px;
  }
  .icon-phone {
    width: 24px;
    height: 24px;
    border-radius: 50%;
    background: var(--paper-white);
  }
  .contact--bottom { left: 565px; top: 838px; }
  .contact--top { left: 670px; top: 78px; transform: rotate(180deg); }
  .contact--left { left: 122px; top: 450px; transform: rotate(90deg); }
  .contact--right { left: 1107px; top: 525px; transform: rotate(-90deg); }
</style>
</head>
<body>
<main class="dieline">
  <svg class="artwork" width="1200" height="962" viewBox="0 0 1200 962" aria-hidden="true">
    <g class="panel-shapes" fill="#ffffff">
      <polygon points="531,203 778,238 957,748 244,728"/>
      <polygon points="181,260 279,251 351,401 181,622"/>
      <polygon points="867,347 1018,287 1018,510"/>
    </g>
    <path class="ribbon" fill="none" stroke="#ffffff" stroke-width="22" stroke-linejoin="round" stroke-linecap="round"
      d="M18,158
         C70,140 120,100 165,100
         C205,100 220,135 270,133
         C330,130 360,80 420,82
         C480,84 510,150 580,155
         C650,160 700,110 780,110
         C850,110 900,160 960,175
         C1010,188 1030,140 1052,150
         C1060,190 1040,220 1075,265
         C1110,310 1090,370 1055,420
         C1010,480 1020,540 1060,610
         C1090,670 1060,760 1045,852
         C980,835 900,855 820,848
         C740,842 690,860 630,895
         C570,935 480,935 420,915
         C360,890 310,860 240,862
         C180,864 140,880 78,855
         C85,790 110,720 120,670
         C130,600 70,560 45,480
         C25,410 70,370 85,320
         C100,260 45,220 18,158 Z"/>
    <g class="fold-lines" stroke="#1a1a1a" stroke-width="1" fill="none">
      <line x1="181" y1="0" x2="181" y2="962"/>
      <line x1="1018" y1="0" x2="1018" y2="962"/>
      <line x1="0" y1="181" x2="1200" y2="181"/>
      <line x1="0" y1="780" x2="1200" y2="780"/>
      <line x1="42" y1="41" x2="138" y2="41"/>
      <line x1="1060" y1="41" x2="1156" y2="41"/>
      <line x1="42" y1="921" x2="138" y2="921"/>
      <line x1="1060" y1="921" x2="1156" y2="921"/>
      <path d="M38,226 A46,46 0 0 1 38,318"/>
      <path d="M38,645 A46,46 0 0 1 38,737"/>
      <path d="M1162,226 A46,46 0 0 0 1162,318"/>
      <path d="M1162,645 A46,46 0 0 0 1162,737"/>
    </g>
  </svg>

  <div class="brand">
    <span class="brand-mark"></span>
    <span class="brand-name">quenby</span>
  </div>

  <div class="contact contact--bottom">
    <div class="contact-row"><span class="icon-handle"></span><span>quenby_z4</span></div>
    <div class="contact-row"><span class="icon-phone"></span><span>95318460</span></div>
  </div>
  <div class="contact contact--top">
    <div class="contact-row"><span class="icon-handle"></span><span>quenby_z4</span></div>
    <div class="contact-row"><span class="icon-phone"></span><span>95318460</span></div>
  </div>
  <div class="contact contact--left">
    <div class="contact-row"><span class="icon-handle"></span><span>quenby_z4</span></div>
    <div class="contact-row"><span class="icon-phone"></span><span>95318460</span></div>
  </div>
  <div class="contact contact--right">
    <div class="contact-row"><span class="icon-handle"></span><span>quenby_z4</span></div>
    <div class="contact-row"><span class="icon-phone"></span><span>95318460</span></div>
  </div>
</main>
</body>
</html>
```